Business Card Design

Electronic Security
Alarm Systems
CCTV
Electronic Access Control
Security System Integration

Industry/Entity Type

Business

Contact Information for Business Card

Gareth Linwood
PO Box 862
Yarrowdale Qld 4173
Phone 07 38265140
Mob 0428637291

```html
<!DOCTYPE html>
<html lang="en">
<head>
<meta charset="utf-8">
<title>Gareth Linwood – Business Card</title>
<link rel="stylesheet" href="https://fonts.googleapis.com/css2?family=Fondamento&family=Ubuntu:ital,wght@0,400;1,500&display=swap">
<style>
  :root {
    --page: #ffffff;
    --card: #63f6fb;
    --glow: #d2fbfc;
    --glow-mid: #a6f8fb;
    --ink: #0d5a5c;
    --ink-dark: #1b2a2b;
    --mobile: #ffc20e;
    --white: #ffffff;
    --bullet-face: #eef6f7;
    --bullet-edge: #b8c9cc;
  }
  * { margin: 0; padding: 0; box-sizing: border-box; }
  html, body {
    width: 1200px; height: 1000px; overflow: hidden;
    background: var(--page);
  }
  .card {
    position: absolute; left: 44px; top: 158px;
    width: 1111px; height: 685px;
    background: var(--card);
    overflow: hidden;
  }
  .card__backdrop {
    position: absolute; left: 104px; top: 17px;
    width: 992px; height: 612px;
    background: radial-gradient(ellipse 70% 65% at 78% 30%, var(--glow) 0%, var(--glow-mid) 45%, rgba(99, 246, 251, 0.4) 100%);
  }
  .card__text { position: absolute; inset: 0; font-family: "Ubuntu", sans-serif; }

  .holder-name {
    position: absolute; left: 106px; top: 108px;
    font-family: "Fondamento", serif; font-weight: 400; font-size: 52px;
    color: var(--ink); white-space: nowrap;
  }
  .mobile {
    position: absolute; left: 106px; top: 188px;
    display: flex; align-items: center; gap: 10px;
  }
  .mobile__icon { width: 36px; height: 36px; }
  .mobile__number {
    font-style: italic; font-weight: 500; font-size: 38px; color: var(--mobile);
    text-shadow: 0 0 2px #fff, 0 0 2px #fff, 1px 1px 1px #fff, -1px -1px 1px #fff;
    white-space: nowrap;
  }
  .services {
    position: absolute; left: 106px; top: 278px;
    list-style: none;
  }
  .services__item {
    display: flex; align-items: center; gap: 12px;
    height: 37.5px;
    font-size: 31px; color: var(--ink); white-space: nowrap;
  }
  .services__bullet { width: 36px; height: 36px; flex: none; }
  .divider {
    position: absolute; left: 106px; top: 518px;
    width: 578px; height: 2px; background: var(--white);
  }
  .address {
    position: absolute; left: 106px; top: 526px;
    font-size: 38.5px; line-height: 49px; color: var(--white);
    font-style: normal; white-space: nowrap;
  }
  .brand {
    position: absolute; left: 806px; top: 262px;
    display: flex; align-items: center; gap: 12px;
  }
  .brand__mark { width: 30px; height: 30px; background: var(--ink-dark); }
  .brand__name {
    font-family: "Ubuntu", sans-serif; font-size: 42px;
    color: var(--ink-dark); letter-spacing: 1px;
  }
</style>
</head>
<body>
  <section class="card">
    <div class="card__backdrop" role="img" aria-label="Soft pale cyan glow decoration behind the card content"></div>

    <div class="card__text">
      <h1 class="holder-name">Gareth Linwood</h1>

      <p class="mobile">
        <svg class="mobile__icon" viewBox="0 0 36 36" aria-hidden="true">
          <circle cx="18" cy="18" r="16" fill="var(--bullet-face)" stroke="var(--bullet-edge)" stroke-width="2"/>
          <rect x="13" y="9" width="10" height="18" rx="2" fill="var(--ink-dark)"/>
          <rect x="15" y="12" width="6" height="6" fill="#e84b3c"/>
        </svg>
        <span class="mobile__number">Mob: 0428637291</span>
      </p>

      <ul class="services">
        <li class="services__item"><svg class="services__bullet" viewBox="0 0 36 36" aria-hidden="true"><circle cx="18" cy="18" r="16" fill="var(--bullet-face)" stroke="var(--bullet-edge)" stroke-width="2"/><polygon points="14,11 25,18 14,25" fill="var(--ink)"/></svg>Electronic Security</li>
        <li class="services__item"><svg class="services__bullet" viewBox="0 0 36 36" aria-hidden="true"><circle cx="18" cy="18" r="16" fill="var(--bullet-face)" stroke="var(--bullet-edge)" stroke-width="2"/><polygon points="14,11 25,18 14,25" fill="var(--ink)"/></svg>Alarm Systems</li>
        <li class="services__item"><svg class="services__bullet" viewBox="0 0 36 36" aria-hidden="true"><circle cx="18" cy="18" r="16" fill="var(--bullet-face)" stroke="var(--bullet-edge)" stroke-width="2"/><polygon points="14,11 25,18 14,25" fill="var(--ink)"/></svg>CCTV</li>
        <li class="services__item"><svg class="services__bullet" viewBox="0 0 36 36" aria-hidden="true"><circle cx="18" cy="18" r="16" fill="var(--bullet-face)" stroke="var(--bullet-edge)" stroke-width="2"/><polygon points="14,11 25,18 14,25" fill="var(--ink)"/></svg>Electronic Access Control</li>
        <li class="services__item"><svg class="services__bullet" viewBox="0 0 36 36" aria-hidden="true"><circle cx="18" cy="18" r="16" fill="var(--bullet-face)" stroke="var(--bullet-edge)" stroke-width="2"/><polygon points="14,11 25,18 14,25" fill="var(--ink)"/></svg>Security System Integration</li>
      </ul>

      <div class="divider"></div>
      <address class="address">
        PO Box 862 Yarrowdale Qld 4173<br>
        Phone: 07 38265140
      </address>

      <div class="brand">
        <span class="brand__mark"></span>
        <span class="brand__name">HALVERN</span>
      </div>
    </div>
  </section>
</body>
</html>
```